Yard sign

Looking for a yard sign. <br/>Something simple, name, number. <br/>Large text, readable from 50 feet away. <br/><br/>18 x 24 inches.

Target Market(s)

Potential homeowners thinking about going solar.

Colors

Designer to choose colors to be used in the design.

Requirements
Must have
• "WE'VE GONE SOLAR!"
Nice to have
• We are a solar company, we would like a design that compliments the homeowners decision that they went solar and encourages others to do the same.

```html
<!DOCTYPE html>
<html lang="en">
<head>
<meta charset="utf-8">
<title>We've Gone Solar – Yard Sign</title>
<link rel="stylesheet" href="https://fonts.googleapis.com/css2?family=Montserrat:wght@500;700;800;900&display=swap">
<style>
  :root {
    --backdrop: #231f20;
    --sign-white: #ffffff;
    --brand-red: #e0301a;
    --brand-orange: #f5730c;
    --brand-amber: #f98a10;
    --sun-yellow: #f9b50f;
    --shadow-grey: #3d3d3d;
  }
  html, body {
    margin: 0;
    padding: 0;
    width: 1200px;
    height: 1200px;
    overflow: hidden;
    background: var(--backdrop);
  }
  .canvas {
    position: relative;
    width: 1200px;
    height: 1200px;
  }
  .yard-sign {
    position: absolute;
    left: 40px;
    top: 180px;
    width: 1120px;
    height: 840px;
    background: var(--sign-white);
  }
  .yard-sign svg {
    display: block;
    width: 1120px;
    height: 840px;
  }
  .headline {
    font-family: "Montserrat", sans-serif;
    font-weight: 900;
  }
  .headline-shadow { fill: var(--shadow-grey); }
  .headline-top { fill: var(--brand-orange); }
  .headline-main { fill: url(#solarGradient); }
  .inner-frame {
    fill: none;
    stroke: var(--brand-red);
    stroke-width: 4;
  }
  .side-block { fill: var(--brand-red); }
  .brand-dot { fill: var(--sun-yellow); }
  .brand-name {
    font-family: "Montserrat", sans-serif;
    font-weight: 800;
    fill: var(--brand-orange);
  }
  .divider { stroke: var(--brand-red); stroke-width: 3; }
  .contact-phone {
    font-family: "Montserrat", sans-serif;
    font-weight: 800;
    fill: var(--brand-red);
  }
  .contact-web {
    font-family: "Montserrat", sans-serif;
    font-weight: 700;
    fill: var(--brand-red);
    letter-spacing: 4px;
  }
</style>
</head>
<body>
<main class="canvas">
  <section class="yard-sign" aria-label="We've gone solar yard sign">
    <svg viewBox="0 0 1120 840" xmlns="http://www.w3.org/2000/svg">
      <defs>
        <linearGradient id="solarGradient" x1="0" y1="0" x2="0" y2="1">
          <stop offset="0.15" stop-color="#e0301a"/>
          <stop offset="0.6" stop-color="#f5730c"/>
          <stop offset="1" stop-color="#f98a10"/>
        </linearGradient>
      </defs>

      <rect class="inner-frame" x="33" y="31" width="1050" height="787" rx="16" ry="16"/>

      <g class="headline">
        <text class="headline-shadow" x="88" y="225" font-size="150" textLength="951" lengthAdjust="spacingAndGlyphs">WE'VE GONE</text>
        <text class="headline-top" x="84" y="221" font-size="150" textLength="951" lengthAdjust="spacingAndGlyphs">WE'VE GONE</text>
        <text class="headline-shadow" x="94" y="454" font-size="262" textLength="945" lengthAdjust="spacingAndGlyphs">SOLAR!</text>
        <text class="headline-main" x="90" y="450" font-size="262" textLength="945" lengthAdjust="spacingAndGlyphs">SOLAR!</text>
      </g>

      <rect class="side-block" x="33" y="562" width="74" height="180"/>
      <rect class="side-block" x="994" y="562" width="91" height="180"/>

      <g class="brand">
        <circle class="brand-dot" cx="170" cy="652" r="32"/>
        <text class="brand-name" x="216" y="670" font-size="46" textLength="290" lengthAdjust="spacingAndGlyphs">SUNRIDGE</text>
      </g>

      <line class="divider" x1="525" y1="602" x2="525" y2="722"/>

      <text class="contact-phone" x="556" y="660" font-size="64" textLength="420" lengthAdjust="spacingAndGlyphs">123 456 7890</text>
      <text class="contact-web" x="556" y="709" font-size="34" textLength="420" lengthAdjust="spacingAndGlyphs">www.sunridgeenergy.net</text>
    </svg>
  </section>
</main>
</body>
</html>
```